Hallo liebe Designer,
wir haben bereits ein Design, welches sich an den Farben unserer Homepage www.kbtr.de orientiert. Dieses Design muss nachgebaut werden. Wir benötigen eine editierbare Microsoft-WORD-Datei, die nach Bedarf angepasst werden kann (falls sich Telefonnummer oder ähnliches mal ändert)
Zusammengefasst:
Benötigt wird: Ein Worddokument mit einem Briefpapier mit der Hauptseite und Folgeseiten. Die Folgeseiten sollen automatisch entstehen, wenn mehr wie 1 Seite beschrieben wird.
Das Design bitte so nachbauen wie es im PDF ersichtlich ist.
- das Worddokument muss anpassbar sein, falls sich mal die Telefonnummer o.ä. ändert

```html
<!DOCTYPE html>
<html lang="de">
<head>
<meta charset="utf-8">
<title>KBT Unternehmensgruppe – Briefpapier</title>
<link rel="stylesheet" href="https://fonts.googleapis.com/css2?family=Poppins:wght@400;500;600&family=Arimo:wght@400&display=swap">
<style>
  :root {
    --backdrop: #f1f1f1;
    --paper: #ffffff;
    --sage: #93ab9d;
    --sage-dark: #6b7d72;
    --text-grey: #5f6f66;
    --rule: #6b7d72;
  }
  * { margin: 0; padding: 0; box-sizing: border-box; }
  html, body {
    width: 1200px; height: 1200px; overflow: hidden;
    background: var(--backdrop);
  }
  .letterhead {
    position: absolute;
    left: 233px; top: 78px;
    width: 733px; height: 1043px;
    background: var(--paper);
    overflow: hidden;
  }
  .brand {
    position: absolute;
    left: 487px; top: 58px;
    font-family: "Poppins", sans-serif;
    color: var(--sage);
  }
  .brand-name {
    display: block;
    font-size: 42px; font-weight: 600;
    line-height: 44px; letter-spacing: 1px;
  }
  .brand-tagline {
    display: block;
    margin-left: 53px; margin-top: 2px;
    font-size: 16.5px; font-weight: 500;
    line-height: 20px;
  }
  .footer-col {
    position: absolute;
    top: 930px;
    color: var(--text-grey);
  }
  .footer-col p { white-space: nowrap; }
  .col-management {
    left: 46px;
    font-family: "Poppins", sans-serif;
    font-size: 8.4px; line-height: 11.6px; font-weight: 500;
  }
  .col-management .register { font-size: 9.6px; font-weight: 600; }
  .col-bank {
    left: 199px; top: 929px;
    font-family: "Poppins", sans-serif;
    font-size: 8.1px; line-height: 11.6px; font-weight: 500;
  }
  .col-bank .bank-name { font-size: 8.8px; }
  .col-bank .iban { font-size: 7.2px; line-height: 9px; }
  .col-address {
    left: 365px; top: 928px;
    font-family: "Arimo", sans-serif;
    font-size: 11.2px; line-height: 13.4px;
  }
  .col-address .contact {
    font-size: 10px; line-height: 11px;
    display: flex; align-items: center; gap: 6px;
  }
  .col-address .contact svg { flex: none; }
  .col-address .contact.mail { gap: 13px; }
  .divider {
    position: absolute;
    top: 928px; width: 1.2px; height: 65px;
    background: var(--rule);
  }
  .divider-one { left: 178px; }
  .divider-two { left: 354px; }
  .footer-band {
    position: absolute; left: 0; bottom: 0;
    width: 733px; height: 54px;
  }
  .web-address {
    position: absolute;
    left: 568px; top: 1003px;
    font-family: "Arimo", sans-serif;
    font-size: 17px; line-height: 20px;
    color: #ffffff;
  }
</style>
</head>
<body>
  <div class="letterhead">
    <div class="brand">
      <span class="brand-name">KBT</span>
      <span class="brand-tagline">Unternehmensgruppe</span>
    </div>

    <div class="footer-col col-management">
      <p>Geschäftsführung:</p>
      <p>Markus Feldberg</p>
      <p>Sabine Lohrmann</p>
      <p>Amtsgericht Lindenfeld</p>
      <p class="register">HRB 48317</p>
    </div>
    <div class="divider divider-one"></div>

    <div class="footer-col col-bank">
      <p>Umsatzsteuer-ID</p>
      <p>DE318274605</p>
      <p>BIC: NORDDEFFXXX</p>
      <p class="bank-name">Rheinbank Solingen</p>
      <p class="bank-name">BIC: RHBKDEDDXXX</p>
      <p class="iban">IBAN: DE12 3456 0110 2233 4455 66</p>
    </div>
    <div class="divider divider-two"></div>

    <div class="footer-col col-address">
      <p>Postanschrift:</p>
      <p>Ahornweg 14</p>
      <p>51643 Talstadt</p>
      <p class="contact phone">
        <svg width="9" height="9" viewBox="0 0 24 24" aria-hidden="true"><path fill="#5f6f66" d="M6.6 10.8a15.1 15.1 0 0 0 6.6 6.6l2.2-2.2c.3-.3.7-.4 1-.2 1.1.4 2.3.6 3.6.6.6 0 1 .4 1 1V20c0 .6-.4 1-1 1A17 17 0 0 1 3 4c0-.6.4-1 1-1h3.5c.6 0 1 .4 1 1 0 1.3.2 2.5.6 3.6.1.3 0 .7-.2 1z"/></svg>
        +49 221 / 45678120
      </p>
      <p class="contact mail">
        <svg width="10" height="7" viewBox="0 0 20 14" aria-hidden="true"><rect x="1" y="1" width="18" height="12" fill="none" stroke="#5f6f66" stroke-width="1.4"/><path d="M1 1l9 7 9-7M1 13l7-6M19 13l-7-6" fill="none" stroke="#5f6f66" stroke-width="1.2"/></svg>
        info@kbtr.de
      </p>
    </div>

    <svg class="footer-band" viewBox="0 0 733 54" aria-hidden="true">
      <rect x="0" y="27" width="733" height="27" fill="var(--sage)"/>
      <polygon points="515,0 733,0 733,54 484,54" fill="var(--sage-dark)"/>
    </svg>
    <div class="web-address">www.kbtr.de</div>
  </div>
</body>
</html>
```